Cruise price comparison web design project

The project's name is Wellenfuchsportal.
www.wellenfuchsportal.de
The current design (which I don't really like) can be found here:
http://wfp02.wellenfuchsportal.de/

I m not too happy with what the current developers have been done so far (in terms of design), so I hope to find a great designer her to develop a design that kicks arses. : )

We are currently developing a site for the German market that brings travel agents and cruise holiday makers together. We are not an ordinary travel agency.
Wellenfuchsportal is a quick and convenient way to have independent travel agencies compete to offer our site visitors the best cruise deal available in Europe.

Here is a short video that explains what one of our competitors does; it gives a good overview as our site will be similar:
http://www.voyabidder.com/video_how_voyabidder_works.php
(Voyabidder.com is not a great website in terms of design, so please dont get me wrong.)

The logo has already been created, but both the colours (should remain blueish) and the font can be modified. The font colour can be changed dramatically if you think this is of advantage.

The Website design should be professional and unique and become an eye catcher. It must attract visitors of all age groups, a "wow-effect" is definitely a bonus.
Users should easily see what this website is about.

We need the following text on our homepage:

"Immer der beste Preis -
denn Reisebüros kämpfen um Sie!"
(means "Always the best rate - as travel agents compete offer the best deal")
This is a sort of headline.

We also need:

So funktioniert Wellenfuchsportal:
1. Wunschkreuzfahrt wählen
2. Angebote erhalten und vergleichen
3. Reisebüro kontaktieren und buchen

(This explains briefly how our system works.)

Aside banners maybe needed later for advertising.

Additions I need on the front page are:
- Login / Sign-Up / Your benefits
(I quite like the way it's done on http://www.lirmatimes.com, at the very top of the page)
- Recommendation-link
(for everything else: Pls. refer to wfp02.wellenfuchsportal.de
- 3 or 4 "top offers of the week"
(current format is not very appealing; offers can be displayed as on http://sailings.tripnuvo.com/affiliate/promo.rvlx?OfferID=DOLUMA27 or

A maritime look is surely an option here, as we focus on cruises. But maybe you can surprise me with a great idea.

I quite like the designs where basically one photo / picture is used.
Some examples which look great IMHO:
http://pell-works.artfolioz.com/art/Glint-Swimmers-519304826
http://quorvanwebdesign.artfolioz.com/art/Website-Design-736152940
The following designer has also done a great job:
http://pixelmaker4387.artfolioz.com/gallery/

ATTACHED:
- logo
- Glint-Swimmers Design .png
- Flyer we use to attract travel agencies
- photo we use for the flyer (we own the rights)

Please get in touch with me if there are any questions or if you require further details. I ll get back to all inquiries / messages as soon as possible, usually within a few hours... Feel free to ask technical questions, too, (if any), the developer will be of assistance.

Reason: I decided to extend the deadline to have more time to comment on your designs and allow you to submit a few more proposals.

Reason: Sorry, more time needed to comment on all designs. Apart from this, some designers asked for more time.

Dear All,

Thank you so much for all your proposals.
Later today I will have a decent internet connection connection again, so I will be able to finally comment on your ideas and visions.

Hopefully next week we can finalize this project. Feel free to submit more designs or ask any questions if there are any.
Remember: Wellenfuchsportal won't be an ordinary travel agent. It brings cruise holiday makers and travel agents together.

Best

Target Market(s)

Holidaymakers / potential cruise holiday makers between 20 and 80.

Industry/Entity Type

Advertising

Requirements
Should not have
• Design should not use old-style, serif fonts.

```html
<!DOCTYPE html>
<html lang="de">
<head>
<meta charset="utf-8">
<title>Wellenfuchsportal – Kreuzfahrten vergleichen</title>
<link href="https://fonts.googleapis.com/css2?family=Questrial&family=Noto+Sans:ital,wght@0,400;0,700;1,400&display=swap" rel="stylesheet">
<style>
:root{
  --sky-top:#3d6fa8;--sky-mid:#8fb4d6;--sea:#1f5ea8;--sea-deep:#0d3f8c;--deck:#b58a62;
  --teal:#4fb7b8;--teal-light:#a7dcdc;--navy:#0b2a5c;--blue-link:#1a55a8;
  --panel:rgba(225,232,245,.82);--panel-dark:rgba(20,50,110,.82);
  --btn:#3f4fd6;--btn-light:#6b79ee;--select:#3b7fe0;--price-tag:#f3e21a;
  --red:#e01010;--yellow:#f6e21a;--white:#fff;--ink:#111;
}
*{box-sizing:border-box;margin:0;padding:0}
html,body{width:933px;height:1200px;overflow:hidden}
body{font-family:"Noto Sans",Verdana,sans-serif;color:var(--ink);position:relative}
.abs{position:absolute}
.backdrop{position:absolute;inset:0;background:
  linear-gradient(180deg,var(--sky-top) 0%,var(--sky-mid) 12%,#c9d9e4 19%,var(--sea) 22%,var(--sea) 50%,#7d8fa6 56%,var(--deck) 66%,#caa27c 69%,var(--sea-deep) 70%,#1b63c0 85%,var(--sea-deep) 100%)}
.heading{font-family:"Questrial",sans-serif}
/* top */
.account-links{left:150px;top:3px;font-size:9px;color:var(--white);display:flex;gap:10px}
.account-links span::before{content:"";display:inline-block;width:7px;height:8px;background:var(--teal-light);margin-right:4px;vertical-align:-1px;border-radius:1px}
.claim{left:159px;top:17px;width:638px;height:22px;background:linear-gradient(#5fd0d0,#2aa7aa);border-radius:2px;color:var(--navy);font-family:"Questrial",sans-serif;font-size:17px;text-align:center;line-height:22px;letter-spacing:.5px}
.brand{left:183px;top:70px;display:flex;align-items:center;gap:8px;color:var(--white);font-family:"Questrial",sans-serif;font-size:20px}
.brand i{width:22px;height:22px;border-radius:50%;background:var(--blue-link);display:block}
.howto{left:493px;top:49px;color:var(--white);font-family:"Questrial",sans-serif}
.howto h2{font-size:15px;font-weight:700;border-bottom:1px solid rgba(255,255,255,.7);padding-bottom:2px;width:265px}
.howto h2::before{content:"• "}
.howto ol{list-style:none;margin:6px 0 0 30px;color:var(--blue-link);font-size:15.5px;line-height:18.5px;letter-spacing:.5px}
.howto li::before{content:"";display:inline-block;border-left:6px solid var(--white);border-top:4px solid transparent;border-bottom:4px solid transparent;margin:0 8px 1px -14px}
.main-nav{left:133px;top:138px;width:668px;height:41px;background:linear-gradient(#bfe8e8,#5eb8bc);border-radius:3px;display:flex;align-items:center;font-family:"Questrial",sans-serif;font-size:15px;color:var(--ink);box-shadow:0 2px 4px rgba(0,0,0,.3)}
.main-nav a{padding:0 18px;text-decoration:none;color:inherit}
.main-nav a.active{margin-left:26px;background:linear-gradient(#fff,#e6e6e6);color:var(--teal);height:32px;line-height:32px;width:96px;text-align:center;border-radius:2px;padding:0}
/* carousel */
.carousel{left:138px;top:260px;width:660px;height:253px;background:rgba(225,232,245,.75);border-radius:4px}
.arrow{width:34px;height:34px;border-radius:50%;background:rgba(255,255,255,.85);top:103px}
.arrow svg{display:block}
.offer-card{top:8px;width:179px;height:237px;background:var(--white);box-shadow:0 0 3px rgba(0,0,0,.4);font-size:8.5px}
.offer-card h3{height:28px;background:linear-gradient(#8fd6d5,#4fb1b2);font-family:"Questrial",sans-serif;font-weight:400;font-size:12.5px;line-height:12px;text-align:center;display:flex;align-items:center;justify-content:center;border-bottom:6px solid #fff;box-shadow:0 6px 0 -4px #5a8fa5}
.offer-card .photo{margin-top:4px;height:108px;background:linear-gradient(#8db7d9,#dfe8ef 60%,#3d79b0);position:relative}
.offer-card .tag{position:absolute;right:0;top:10px;background:var(--price-tag);color:var(--red);font-weight:700;font-size:12.5px;padding:1px 4px 1px 14px;clip-path:polygon(10px 0,100% 0,100% 100%,10px 100%,0 50%)}
.offer-card .tag small{font-weight:400;font-size:11px}
.offer-card .ship{position:absolute;bottom:0;left:0;right:0;height:18px;background:rgba(0,0,0,.35);color:var(--white);font-family:"Questrial",sans-serif;font-size:13px;text-align:center;line-height:18px;letter-spacing:.5px}
.offer-card .body{padding:4px 7px;line-height:11px}
.offer-card .body a{color:var(--blue-link)}
.offer-card .date{color:var(--red);margin-top:7px}
.offer-card .order{position:absolute;left:4px;right:4px;bottom:3px;height:19px;background:linear-gradient(var(--btn-light),var(--btn));color:var(--white);font-family:"Questrial",sans-serif;font-size:13px;text-align:center;line-height:19px;border-radius:2px;letter-spacing:.5px}
/* testimonials */
.testimonials{left:142px;top:530px;width:247px;height:328px;background:var(--panel)}
.testimonials h2{font-family:"Questrial",sans-serif;font-weight:400;font-size:14px;margin:6px 0 0 16px;border-bottom:1px solid #333;width:183px}
.quote{left:14px;width:228px;height:60px}
.quote .avatar{position:absolute;left:0;top:0;width:58px;height:58px;background:linear-gradient(#c9a07a,#6c8b5a)}
.quote p{position:absolute;left:72px;top:6px;width:150px;font-size:7px;font-style:italic;line-height:13px}
.quote b{position:absolute;right:10px;top:45px;font-size:8px}
/* exclusive offers */
.offers-head{left:406px;top:530px;width:392px;height:28px;background:var(--panel-dark);color:var(--white);font-family:"Questrial",sans-serif;font-size:17px;padding:2px 0 0 30px;letter-spacing:.5px}
.offers-head span{color:var(--yellow)}
.offers-head em{position:absolute;right:60px;top:8px;font-size:9px;font-style:italic}
.deal{left:406px;width:392px;height:80px;background:rgba(190,200,230,.8);font-size:8.5px}
.deal .thumb{position:absolute;left:11px;top:7px;width:70px;height:42px;background:linear-gradient(#cfdcec,#5f7ea4);border:2px solid #fff}
.deal .title{position:absolute;left:87px;top:4px;letter-spacing:.3px;font-size:9px;border-bottom:1px solid #333;width:274px}
.deal .line{position:absolute;left:87px;top:16px;font-weight:700}
.deal .cabin{position:absolute;top:30px;text-align:center;line-height:11px}
.deal .cabin u{display:block}
.deal .cabin b{color:var(--red);font-weight:400}
.deal .select{position:absolute;left:275px;top:31px;width:53px;height:20px;background:linear-gradient(#6aa6f0,var(--select));color:#fff;font-weight:700;font-size:11px;text-align:center;line-height:20px;border-radius:2px}
.deal .note{position:absolute;left:75px;top:60px;color:var(--red);font-weight:700;font-size:7.5px;letter-spacing:.3px}
.deal .note::before{content:"● "}
/* booking */
.booking{left:135px;top:866px;width:257px;height:334px;background:var(--panel-dark);color:var(--white)}
.booking h2{font-family:"Questrial",sans-serif;font-weight:400;font-size:17px;margin:13px 0 0 9px;border-bottom:1px solid #fff;width:240px;letter-spacing:.5px}
.booking h2 span,.booking h3 span{color:var(--yellow)}
.field{left:14px;font-size:9px;font-weight:700}
.select-box{position:absolute;left:220px;height:13px;background:#fff;color:#222;font-size:8px;font-weight:400;text-align:center;line-height:13px;border:1px solid #5d7fb8}
.select-box::after{content:"";position:absolute;right:0;top:0;width:14px;height:11px;background:#4f8ad8}
.go{left:180px;top:146px;width:52px;height:18px;background:linear-gradient(#6aa6f0,var(--select));font-size:11px;font-weight:700;text-align:center;line-height:18px;border-radius:2px}
.booking h3{position:absolute;left:10px;top:182px;font-family:"Questrial",sans-serif;font-weight:400;font-size:15px}
.booking .about{position:absolute;left:10px;top:204px;width:235px;font-size:8px;line-height:13.5px}
.booking .more{position:absolute;right:20px;top:240px;color:var(--yellow);font-size:8px}
.booking .links a{position:absolute;left:10px;color:#fff;text-decoration:none;font-family:"Questrial",sans-serif;font-size:14px;width:240px;border-top:1px solid rgba(255,255,255,.5)}
.booking .links a::after{content:" ▸";color:var(--yellow);font-size:11px}
/* footer */
.foot-col{font-size:9.5px;color:var(--white)}
.foot-col h4{font-family:"Questrial",sans-serif;font-weight:700;font-size:12.5px;border-bottom:1px solid #fff;width:190px;margin-bottom:4px}
.foot-col a{display:block;color:var(--white);text-decoration:none;width:185px;border-bottom:1px dashed rgba(255,255,255,.6);padding:4px 0 4px}
.foot-col a::after{content:" ▸";font-size:8px}
.social{top:1135px;width:31px;height:31px;background:#4a6fb0;border-radius:3px}
</style>
</head>
<body>
<div class="backdrop" role="img" aria-label="Full-page photo: cloudy sky over a tropical island, open sea with leaping dolphins, a sunny cruise ship deck with people, and an underwater scene with fish and a diver"></div>

<nav class="abs account-links"><span>Login</span><span>Sign Up</span><span>Your Benefits</span></nav>
<div class="abs claim">Immer der beste Preis denn Reisebüros kämpfen um Sie</div>
<div class="abs brand"><i></i>Wellenfuchsportal</div>
<section class="abs howto">
  <h2>So funktioniert Wellenfuchsportal:</h2>
  <ol><li>Wunschkreuzfahrt wählen</li><li>Angebote erhalten und vergleichen</li><li>Reisebüro kontaktieren und buchen</li></ol>
</section>
<nav class="abs main-nav">
  <a class="active" href="#">So Gehts</a><a href="#">Angebote erhalten</a><a href="#">Reedereien und Schiffe</a><a href="#">Specials</a><a href="#">Kontakt</a>
</nav>

<section class="abs carousel">
  <div class="abs arrow" style="left:9px"><svg width="34" height="34"><path d="M20 9 L11 17 L20 25" fill="none" stroke="#7a8fb0" stroke-width="4"/></svg></div>
  <div class="abs arrow" style="left:614px"><svg width="34" height="34"><path d="M14 9 L23 17 L14 25" fill="none" stroke="#7a8fb0" stroke-width="4"/></svg></div>
  <article class="abs offer-card" style="left:51px">
    <h3>Off the city to Big Apple</h3>
    <div class="photo" role="img" aria-label="Cruise ship at sea under a blue sky"><span class="tag">€ 2,899 <small>/Person</small></span><span class="ship">Regatta of Sea</span></div>
    <div class="body"><a href="#">Incl. Luftkranich flights, transfers and hotel accommodation in Buenos Aires</a><div style="margin-top:6px">22 days South America Cruise</div><div style="color:var(--red)">Appointment in July 2012</div></div>
    <div class="order">Sample Order</div>
  </article>
  <article class="abs offer-card" style="left:239px">
    <h3>Around Iceland from/<br>to Hamburg</h3>
    <div class="photo" role="img" aria-label="Cruise ship in front of snowy mountains"><span class="tag">€ 1,300 <small>/Person</small></span><span class="ship">Saga of Seas</span></div>
    <div class="body"><a href="#">12 days Iceland tour</a><div class="date">Date: 26.06.2012</div></div>
    <div class="order">Sample Order</div>
  </article>
  <article class="abs offer-card" style="left:428px">
    <h3>Lorem ipsum dolor sit</h3>
    <div class="photo" role="img" aria-label="Palm trees on a tropical beach"><span class="tag">€ 1,300 <small>/Person</small></span><span class="ship">Quis nostrud</span></div>
    <div class="body"><a href="#">12 days Iceland tour</a><div class="date">Date: 26.06.2012</div></div>
    <div class="order">Sample Order</div>
  </article>
</section>

<section class="abs testimonials">
  <h2>Testimonials</h2>
  <div class="abs quote" style="top:30px"><div class="avatar" role="img" aria-label="Portrait photo of a smiling couple"></div><p>Lorem Ipsum is simply dummy text of the printim Ipsum has been the industry's standard dummy and typesetting industry</p><b>---------- Lorem Ipsum</b></div>
  <div class="abs quote" style="top:96px"><div class="avatar" role="img" aria-label="Portrait photo of a smiling couple"></div><p>Lorem Ipsum is simply dummy text of the printim Ipsum has been the industry's standard dummy and typesetting industry</p><b>---------- Lorem Ipsum</b></div>
  <div class="abs quote" style="top:168px"><div class="avatar" role="img" aria-label="Portrait photo of a smiling couple"></div><p>Lorem Ipsum is simply dummy text of the printim Ipsum has been the industry's standard dummy and typesetting industry</p><b>---------- Lorem Ipsum</b></div>
  <div class="abs quote" style="top:240px"><div class="avatar" role="img" aria-label="Portrait photo of a smiling couple"></div><p>Lorem Ipsum is simply dummy text of the printim Ipsum has been the industry's standard dummy and typesetting industry</p><b>---------- Lorem Ipsum</b></div>
</section>

<header class="abs offers-head">Exclusive <span>Offers ▸</span><em>View More ▸</em></header>
<div class="abs deal" style="top:565px"><div class="thumb" role="img" aria-label="Cruise ship photo"></div><div class="title">15 Dec 2012 - 7-day Eastern Caribbean From Miami</div><div class="line">Nordwind Cruise Line - Nordwind Aurora</div><div class="cabin" style="left:100px"><u>Inside</u><b>$550</b></div><div class="cabin" style="left:150px"><u>Balcony</u><b>$750</b></div><div class="cabin" style="left:211px"><u>Suite</u><b>$950</b></div><div class="select">Select</div><div class="note">Free bottle of sparkling wine and chocolate strawberries</div></div>
<div class="abs deal" style="top:652px"><div class="thumb" role="img" aria-label="Cruise ship photo"></div><div class="title">15 Dec 2012 - 7-day Eastern Caribbean From Miami</div><div class="line">Nordwind Cruise Line - Nordwind Aurora</div><div class="cabin" style="left:100px"><u>Inside</u><b>$550</b></div><div class="cabin" style="left:150px"><u>Balcony</u><b>$750</b></div><div class="cabin" style="left:211px"><u>Suite</u><b>$950</b></div><div class="select">Select</div><div class="note">Free bottle of sparkling wine and chocolate strawberries</div></div>
<div class="abs deal" style="top:739px"><div class="thumb" role="img" aria-label="Cruise ship photo"></div><div class="title">15 Dec 2012 - 7-day Eastern Caribbean From Miami</div><div class="line">Nordwind Cruise Line - Nordwind Aurora</div><div class="cabin" style="left:100px"><u>Inside</u><b>$550</b></div><div class="cabin" style="left:150px"><u>Balcony</u><b>$750</b></div><div class="cabin" style="left:211px"><u>Suite</u><b>$950</b></div><div class="select">Select</div><div class="note">Free bottle of sparkling wine and chocolate strawberries</div></div>
<div class="abs deal" style="top:826px"><div class="thumb" role="img" aria-label="Cruise ship photo"></div><div class="title">15 Dec 2012 - 7-day Eastern Caribbean From Miami</div><div class="line">Nordwind Cruise Line - Nordwind Aurora</div><div class="cabin" style="left:100px"><u>Inside</u><b>$550</b></div><div class="cabin" style="left:150px"><u>Balcony</u><b>$750</b></div><div class="cabin" style="left:211px"><u>Suite</u><b>$950</b></div><div class="select">Select</div><div class="note">Free bottle of sparkling wine and chocolate strawberries</div></div>
<div class="abs deal" style="top:913px"><div class="thumb" role="img" aria-label="Cruise ship photo"></div><div class="title">15 Dec 2012 - 7-day Eastern Caribbean From Miami</div><div class="line">Nordwind Cruise Line - Nordwind Aurora</div><div class="cabin" style="left:100px"><u>Inside</u><b>$550</b></div><div class="cabin" style="left:150px"><u>Balcony</u><b>$750</b></div><div class="cabin" style="left:211px"><u>Suite</u><b>$950</b></div><div class="select">Select</div><div class="note">Free bottle of sparkling wine and chocolate strawberries</div></div>

<aside class="abs booking">
  <h2>Book Your <span>Cruise Packages</span></h2>
  <div class="abs field" style="top:46px">Desitination<span class="select-box" style="left:221px;left:86px;width:134px;top:0">Select Destination</span></div>
  <div class="abs field" style="top:71px">Depature Date<span class="select-box" style="left:86px;width:134px;top:0">Select Departure date</span></div>
  <div class="abs field" style="top:96px">No. of Cabins<span class="select-box" style="left:86px;width:34px;top:0;text-align:left;padding-left:4px">1</span></div>
  <div class="abs field" style="top:121px">Departure Port<span class="select-box" style="left:86px;width:134px;top:0">Departure Port</span></div>
  <div class="abs go">Go</div>
  <h3>About <span>Us</span></h3>
  <p class="about">Lorem ipsum dolor sit amet, consectetur adipisicing elit, sed do eiusmod tempor incididunt ut labore et dolore magna aliqua. Ut enim ad minim veniam, quis</p>
  <span class="more">More ▸</span>
  <div class="links"><a href="#" style="top:256px">Jobs</a><a href="#" style="top:276px">Partners</a><a href="#" style="top:298px">Advertise Wellenfuchsportal.de</a></div>
</aside>

<nav class="abs foot-col" style="left:405px;top:1008px">
  <h4>Press</h4><a href="#">Press Materials</a><a href="#">Wellenfuchs in the media</a><a href="#">Press Releases</a><a href="#">Wellenfuchs and the social media</a>
</nav>
<nav class="abs foot-col" style="left:405px;top:1120px">
  <h4>Disclaimer</h4><a href="#">Disclaimer / disclaimer</a><a href="#">Terms of Services</a><a href="#">Impressum</a>
</nav>
<nav class="abs foot-col" style="left:615px;top:1008px">
  <h4>Help &amp; Support</h4><a href="#">Product Reviews</a><a href="#">Contact</a><a href="#">FAQ's</a>
</nav>
<span class="abs social" style="left:660px"></span>
<span class="abs social" style="left:698px"></span>
</body>
</html>
```